Passionate Homecare Agency Needs an "Employee News" Webpage Design

We are a homecare agency with more than 300 employees who provide personal care and assistance with the activities of daily living in clients’ homes. Our company slogan is “Someone you can depend on… Without question.” We strive to provide our clients with the highest quality, compassionate care possible, and we want our employees to feel inspired to do just that.

We are looking for an employee web page design to add to our existing website that makes our field employees feel connected to the company, is fun and energetic, and provides our caregivers with helpful information, employee news, and recognition. We want this to be a hub for communication and celebration, and also showcase our appreciation for all that they do!

We look forward to your designs! The sky's the limit!
Updates

Reason: Looking for a few more designs that fit our descriptions before making a final decision.

Target Market(s)

Our Employees

Industry/Entity Type

Home Health Care

Number of Pages Required

1 page

Colors

Designer to choose colors to be used in the design.

Requirements
Must have
• We would like to have sections like:
• -Employee of the Month/Week
• -Caregiver Tips and Tricks
• -Birthdays and Anniversaries
• -New Employees
• -Area to add links to our social media (Facebook, Instagram, Twitter)
• -etc!
Nice to have
• Bright colors and fun themes.

```html
<!DOCTYPE html>
<html lang="en">
<head>
<meta charset="utf-8">
<title>Harbor Care Group – Employee Hub</title>
<link href="https://fonts.googleapis.com/css2?family=Raleway:wght@400;500;600;700;800&display=swap" rel="stylesheet">
<style>
:root{
  --blue:#1a7be6;
  --teal:#5e9393;
  --teal-dark:#1f6868;
  --ink:#1d2a33;
  --muted:#6b7680;
  --band:#e5eef1;
  --line:#d9e0e4;
  --white:#fff;
}
*{box-sizing:border-box;margin:0;padding:0}
html,body{width:1200px;height:1200px;overflow:hidden;background:#fff;font-family:'Raleway',sans-serif;color:var(--ink)}
.page{position:absolute;left:366px;top:0;width:468px;height:1200px;background:#fff}
.abs{position:absolute}
.tiny{font-size:4.2px;line-height:7px;color:var(--muted)}
.h-sec{font-size:8.5px;font-weight:800;letter-spacing:.3px;color:var(--ink);white-space:nowrap}
.h-sub{font-size:4.4px;letter-spacing:.4px;color:var(--ink);text-transform:uppercase;white-space:nowrap}
.pill{position:absolute;background:var(--blue);color:#fff;border-radius:8px;font-size:4px;font-weight:600;display:flex;align-items:center;justify-content:center;letter-spacing:.3px;text-transform:uppercase;white-space:nowrap}

/* header */
.topline{font-size:4.6px;color:var(--ink);top:16px;white-space:nowrap}
.brand{left:204px;top:4px;width:60px;text-align:center}
.brand .dot{display:block;width:9px;height:9px;border-radius:50%;background:var(--ink);margin:0 auto 1px}
.brand .name{font-size:10px;font-weight:700;color:var(--ink);line-height:12px}
.nav{left:0;top:35px;width:468px;height:15px;background:var(--teal)}
.nav a{position:absolute;top:0;height:15px;line-height:15px;font-size:4.4px;color:#e8f1f1;text-decoration:none;letter-spacing:.2px;white-space:nowrap}
.nav a.active{background:var(--teal-dark);width:35px;text-align:center}
.nav .search{position:absolute;left:394px;top:3px;width:10px;height:9px;background:#fff}

/* hero – employee of the month */
.hero{left:0;top:50px;width:468px;height:160px;background:linear-gradient(120deg,#2a8af0,#1870de);overflow:hidden}
.hero h1{position:absolute;left:63px;top:29px;font-size:18.5px;font-weight:700;color:#fff;letter-spacing:.2px;white-space:nowrap}
.hero h2{position:absolute;left:63px;top:50px;font-size:10px;font-weight:400;color:#fff;white-space:nowrap}
.hero p{position:absolute;left:63px;top:70px;width:170px;font-size:4.4px;line-height:7.2px;color:#dbe9fb}
.hero .btn-outline{position:absolute;left:63px;top:109px;width:105px;height:18px;border:1px solid #fff;border-radius:10px;color:#fff;font-size:6.4px;display:flex;align-items:center;justify-content:center;white-space:nowrap}
.hero .photo{position:absolute;left:266px;top:4px;width:140px;height:156px;border-radius:60px 60px 0 0;background:linear-gradient(180deg,#6ec7dc 0%,#42b4d6 55%,#2aa2cf 100%)}

/* tips */
.photo-block{background:linear-gradient(135deg,#dfe8ef,#b9c9dc 45%,#7e9fd2)}
.svc-icon{position:absolute;width:19px;height:19px;background:var(--blue);display:flex;align-items:center;justify-content:center}
.svc-title{font-size:6px;color:var(--ink);font-weight:500;white-space:nowrap}

/* bands */
.band{left:0;width:468px;background:var(--band)}
.avatar{position:absolute;width:38px;height:38px;border-radius:50%;border:1.5px solid #fff}

/* news */
.feat-icon{position:absolute;width:20px;height:20px;background:#e7edf1;display:flex;align-items:center;justify-content:center}
.feat-title{font-size:5.6px;color:var(--ink);white-space:nowrap}

/* new employees */
.card{position:absolute;top:802px;width:77px;height:117px;background:#fff}
.card.raised{box-shadow:0 3px 8px rgba(0,0,0,.12)}
.card .ph{width:77px;height:81px}
.card .nm{position:absolute;left:8px;top:91px;font-size:3.8px;font-weight:600;color:var(--ink);white-space:nowrap}
.card .rl{position:absolute;left:8px;top:97px;font-size:3.8px;color:var(--blue);white-space:nowrap}
.card .soc{position:absolute;left:8px;top:104px;display:flex;gap:3px}
.soc i{display:block;width:3.5px;height:3.5px;border-radius:50%;background:#9aa6ae}

/* slogan */
.cta-title{left:0;width:468px;top:973px;text-align:center;font-size:10px;font-weight:500;color:var(--ink)}
.cta-title b{color:var(--blue);font-weight:800}
.cta-text{left:114px;width:242px;top:991px;text-align:center;font-size:4.7px;line-height:7px;color:#3b4750}

/* footer */
.f-head{font-size:5.4px;color:var(--ink)}
.f-link{font-size:3.8px;color:#9aa3aa;letter-spacing:.3px;text-transform:uppercase;white-space:nowrap}
.f-logo{font-size:8px;font-weight:700;color:var(--ink);display:flex;align-items:center;gap:2px}
.f-logo i{display:block;width:5px;height:5px;border-radius:50%;background:var(--teal)}
.bottom{left:0;top:1180px;width:468px;height:20px;background:var(--blue);color:#fff;font-size:4px;display:flex;align-items:center;justify-content:center}
</style>
</head>
<body>
<div class="page">

  <!-- header -->
  <div class="abs topline" style="left:63px">Email Us : hello@harborcare.org</div>
  <div class="abs brand"><span class="dot"></span><span class="name">Harbor</span></div>
  <div class="abs topline" style="left:330px;width:76px;text-align:right">Call Us : 555-014-2290</div>

  <nav class="abs nav">
    <a class="active" style="left:63px">HOME</a>
    <a style="left:106px">OPEN SHIFTS</a>
    <a style="left:152px">EMPLOYEE NEWS</a>
    <a style="left:207px">MY SKILLS</a>
    <a style="left:247px">EMPLOYEE FORMS</a>
    <a style="left:304px">CONTACT US</a>
    <span class="search"><svg width="10" height="9" viewBox="0 0 10 9"><circle cx="4.6" cy="4" r="1.8" fill="none" stroke="#444" stroke-width=".6"/><line x1="5.9" y1="5.3" x2="7" y2="6.4" stroke="#444" stroke-width=".6"/></svg></span>
  </nav>

  <!-- employee of the month -->
  <section class="abs hero">
    <h1>CAREGIVER STAR</h1>
    <h2>EMPLOYEE OF THE MONTH: ANA REYES</h2>
    <p>Ana has brought warmth and steady care to her clients for four years. Families say she turns every visit into the best part of their day. Thank you, Ana, for being someone they can depend on.</p>
    <div class="btn-outline">READ HER STORY</div>
    <div class="photo" role="img" aria-label="Employee of the month portrait, caregiver in blue scrubs with a stethoscope"></div>
  </section>

  <!-- caregiver tips -->
  <div class="abs h-sec" style="left:66px;top:231px">CAREGIVER TIPS AND TRICKS</div>
  <div class="abs h-sub" style="left:66px;top:241px">Ideas from the field</div>
  <p class="abs tiny" style="left:66px;top:256px;width:182px">Every week our caregivers share the small ideas that make home visits smoother. Start each shift with a quick chat about how your client slept, keep a notebook by the door for family notes, and plan meals together so clients stay part of the choice. Small routines build trust, keep everyone safe and make each day a little brighter.</p>
  <div class="abs photo-block" style="left:67px;top:307px;width:171px;height:88px" role="img" aria-label="Group of smiling caregivers and a nurse standing together"></div>

  <div class="svc-icon" style="left:267px;top:233px"><svg width="10" height="9" viewBox="0 0 10 9" fill="none" stroke="#fff" stroke-width=".7"><path d="M1 8h8M2.5 8V5M5 8V3M7.5 8V1"/></svg></div>
  <div class="abs svc-title" style="left:295px;top:232px">Safe transfers and lifting</div>
  <p class="abs tiny" style="left:295px;top:240px;width:130px">Bend at the knees, keep your client close and count down together before every move. Use a gait belt whenever one is in the care plan.</p>

  <div class="svc-icon" style="left:267px;top:276px"><svg width="9" height="10" viewBox="0 0 9 10" fill="none" stroke="#fff" stroke-width=".7"><rect x="1" y="1.5" width="7" height="8"/><path d="M3 1.5V.6h3v.9M2.5 4h4M2.5 6h4M2.5 8h3"/></svg></div>
  <div class="abs svc-title" style="left:295px;top:274px">Keeping clients hydrated</div>
  <p class="abs tiny" style="left:295px;top:282px;width:130px">Offer a drink at every task change and keep a filled cup within easy reach.</p>

  <div class="svc-icon" style="left:267px;top:312px"><svg width="8" height="11" viewBox="0 0 8 11" fill="none" stroke="#fff" stroke-width=".7"><path d="M1 1h6M1 1l3 4 3-4M4 5v5"/></svg></div>
  <div class="abs svc-title" style="left:295px;top:310px">Easy meals, happy clients</div>
  <p class="abs tiny" style="left:295px;top:318px;width:130px">Batch simple soups on long shifts and label each one with the date so families can follow along.</p>

  <div class="pill" style="left:296px;top:353px;width:50px;height:11px">More tips</div>

  <!-- birthdays and anniversaries -->
  <section class="abs band" style="top:418px;height:136px"></section>
  <div class="abs h-sec" style="left:66px;top:446px">CELEBRATIONS</div>
  <div class="abs h-sub" style="left:66px;top:456px">Birthdays and anniversaries</div>
  <svg class="abs" style="left:66px;top:478px" width="17" height="14" viewBox="0 0 17 14"><path d="M0 14V7C0 3 2 .5 6 0v3C4 3.5 3.5 5 3.5 7H7v7zM10 14V7c0-4 2-6.5 6-7v3c-2 .5-2.5 2-2.5 4H17v7z" fill="var(--ink)"/></svg>
  <p class="abs" style="left:95px;top:477px;width:152px;font-size:3.9px;line-height:7px;color:#2b3640">Happy birthday to Tom, Priya and Jonah this week! We also celebrate Grace on five years and Leo on ten years with our team. Your kindness and care make a difference in so many homes. Please join us in sending them your warmest wishes ...</p>
  <div class="abs" style="left:95px;top:518px;font-size:3.9px;color:#2b3640">By</div>
  <div class="abs" style="left:95px;top:524px;font-size:3.9px;font-weight:700;color:#2b3640">HARBOR HR TEAM</div>
  <div class="abs" style="left:258px;top:468px;width:1px;height:60px;background:#cfd9de"></div>
  <div class="avatar" style="left:267px;top:477px;background:linear-gradient(160deg,#d9dde0,#8d949a)" role="img" aria-label="Birthday portrait, man in grey shirt"></div>
  <div class="avatar" style="left:315px;top:477px;background:linear-gradient(160deg,#f0e6e0,#7a5446)" role="img" aria-label="Anniversary portrait, smiling woman with curly hair"></div>
  <div class="avatar" style="left:362px;top:477px;background:linear-gradient(160deg,#5d6f78,#3d5a6c)" role="img" aria-label="Birthday portrait, bearded man"></div>
  <svg class="abs" style="left:323px;top:519px" width="20" height="4"><circle cx="2" cy="2" r="1.6" fill="var(--blue)"/><circle cx="9" cy="2" r="1.6" fill="#b9c8d4"/><circle cx="16" cy="2" r="1.6" fill="#b9c8d4"/></svg>

  <!-- employee news -->
  <div class="abs h-sec" style="left:66px;top:582px">EMPLOYEE NEWS</div>
  <div class="abs h-sub" style="left:66px;top:592px">What's happening</div>

  <div class="feat-icon" style="left:66px;top:616px"><svg width="11" height="9" viewBox="0 0 11 9" fill="none" stroke="#51606b" stroke-width=".6"><path d="M1 1h9v7H1zM3 1v7M5.5 1v7M8 1v7"/></svg></div>
  <div class="abs feat-title" style="left:95px;top:614px">New open shifts posted</div>
  <p class="abs tiny" style="left:95px;top:623px;width:76px">Weekend and evening visits are open now. Claim yours in the shifts page.</p>

  <div class="feat-icon" style="left:181px;top:616px"><svg width="11" height="9" viewBox="0 0 11 9" fill="none" stroke="#51606b" stroke-width=".6"><path d="M1 4l3-3 3 2 3-1M1 4l4 4 5-4-3-1"/></svg></div>
  <div class="abs feat-title" style="left:210px;top:614px">Training day schedule</div>
  <p class="abs tiny" style="left:210px;top:623px;width:76px">Our spring training day covers dementia care, safe lifting and first aid.</p>

  <div class="feat-icon" style="left:295px;top:616px"><svg width="11" height="10" viewBox="0 0 11 10" fill="none" stroke="#51606b" stroke-width=".6"><circle cx="5.5" cy="2" r="1"/><circle cx="2.5" cy="6" r="1"/><circle cx="8.5" cy="6" r="1"/><path d="M1 9.5h3M7 9.5h3M4 5h3"/></svg></div>
  <div class="abs feat-title" style="left:323px;top:614px">Referral bonus is back</div>
  <p class="abs tiny" style="left:323px;top:623px;width:76px">Bring a friend to the team and earn a thank you bonus after their first month.</p>

  <div class="feat-icon" style="left:66px;top:662px"><svg width="11" height="10" viewBox="0 0 11 10" fill="none" stroke="#51606b" stroke-width=".6"><rect x="1" y="1" width="9" height="6"/><path d="M5.5 7v2M3.5 9.5h4M4 5l1.5-2 1.5 2"/></svg></div>
  <div class="abs feat-title" style="left:97px;top:660px">Skills course unlocked</div>
  <p class="abs tiny" style="left:95px;top:669px;width:76px">A new online course on nutrition is ready in My Skills for every caregiver.</p>

  <div class="feat-icon" style="left:181px;top:662px"><svg width="9" height="11" viewBox="0 0 9 11" fill="none" stroke="#51606b" stroke-width=".6"><rect x="1" y="3" width="7" height="7"/><path d="M3 3V1h3v2M2.5 5.5h4M2.5 7.5h4"/></svg></div>
  <div class="abs feat-title" style="left:210px;top:660px">Updated employee forms</div>
  <p class="abs tiny" style="left:210px;top:669px;width:76px">Time off and mileage forms were refreshed. Please use the new versions.</p>

  <div class="feat-icon" style="left:295px;top:662px"><svg width="11" height="9" viewBox="0 0 11 9" fill="none" stroke="#51606b" stroke-width=".6"><rect x="1" y="2.5" width="9" height="6"/><path d="M4 2.5V1h3v1.5M1 5h9"/></svg></div>
  <div class="abs feat-title" style="left:323px;top:660px">Summer picnic plans</div>
  <p class="abs tiny" style="left:323px;top:669px;width:76px">Save the date for our team picnic with games, food and family fun.</p>

  <div class="pill" style="left:210px;top:709px;width:47px;height:10px">More news</div>

  <!-- new employees -->
  <section class="abs band" style="top:748px;height:200px"></section>
  <div class="abs h-sec" style="left:67px;top:776px">NEW EMPLOYEES</div>
  <div class="abs h-sub" style="left:67px;top:786px">Welcome to the team</div>

  <div class="card" style="left:67px">
    <div class="ph" style="background:linear-gradient(180deg,#9ec7d9,#c9dde6 60%,#eef2f4)" role="img" aria-label="New employee portrait, woman in white coat with stethoscope"></div>
    <div class="nm">LENA MARSH</div><div class="rl">Registered nurse</div>
    <div class="soc"><i></i><i></i><i></i><i></i></div>
  </div>
  <div class="card raised" style="left:153px">
    <div class="ph" style="background:linear-gradient(180deg,#c6d8e2,#e4ecf0 60%,#f5f7f8)" role="img" aria-label="New employee portrait, smiling man with glasses"></div>
    <div class="nm">DAVID OKORO</div><div class="rl">Personal care aide</div>
    <div class="soc"><i></i><i></i><i></i><i></i></div>
  </div>
  <div class="card" style="left:238px">
    <div class="ph" style="background:linear-gradient(180deg,#a9c4dd,#5f86b8 70%,#3f6aa8)" role="img" aria-label="New employee portrait, caregiver in blue scrubs"></div>
    <div class="nm">SOPHIE GRANT</div><div class="rl">Home health aide</div>
    <div class="soc"><i></i><i></i><i></i><i></i></div>
  </div>
  <div class="card" style="left:324px">
    <div class="ph" style="background:linear-gradient(180deg,#5c5a52,#8e8a80 50%,#e7e7e4)" role="img" aria-label="New employee portrait, man in white coat and tie"></div>
    <div class="nm">MARCUS BELL</div><div class="rl">Care coordinator</div>
    <div class="soc"><i></i><i></i><i></i><i></i></div>
  </div>

  <!-- slogan -->
  <div class="abs cta-title">SOMEONE YOU CAN <b>DEPEND ON</b></div>
  <p class="abs cta-text">Thank you for the care you give every single day. Have news to share, a tip for your fellow caregivers or a teammate who deserves a shout out? Send it our way and we will feature it here. Follow us online and stay connected with the whole team.</p>
  <div class="pill" style="left:214px;top:1030px;width:41px;height:10px">Share news</div>

  <!-- footer -->
  <div class="abs" style="left:67px;top:1078px;width:334px;height:1px;background:var(--line)"></div>
  <div class="abs f-logo" style="left:63px;top:1114px"><i></i>Harbor</div>
  <div class="abs f-logo" style="left:63px;top:1150px"><i></i>Harbor</div>

  <div class="abs f-head" style="left:124px;top:1108px">Menu</div>
  <div class="abs f-link" style="left:124px;top:1121px">Home</div>
  <div class="abs f-link" style="left:124px;top:1131px">Open shifts</div>
  <div class="abs f-link" style="left:124px;top:1141px">Employee news</div>
  <div class="abs f-link" style="left:124px;top:1151px">My skills</div>
  <div class="abs f-link" style="left:181px;top:1121px">Service</div>
  <div class="abs f-link" style="left:181px;top:1131px">Employee forms</div>
  <div class="abs f-link" style="left:181px;top:1141px">Contact us</div>
  <div class="abs soc" style="left:181px;top:1152px;display:flex;gap:3px"><i></i><i></i><i></i></div>

  <div class="abs f-head" style="left:238px;top:1108px">Contact</div>
  <div class="abs f-link" style="left:238px;top:1121px"><b style="color:var(--ink)">Address :</b> Maplewood Street</div>
  <div class="abs f-link" style="left:238px;top:1131px">Second floor : 48569</div>
  <div class="abs f-link" style="left:238px;top:1141px"><b style="color:var(--ink)">Phone :</b> +555 0147 222</div>
  <div class="abs f-link" style="left:238px;top:1151px"><b style="color:var(--ink)">Email :</b> team@harborcare.org</div>

  <div class="abs f-head" style="left:324px;top:1108px">Newsletter</div>
  <div class="abs f-link" style="left:324px;top:1121px">Sign up your newsletter</div>
  <div class="abs" style="left:324px;top:1130px;width:64px;height:12px;border:.6px solid var(--line);font-size:3.6px;color:#9aa3aa;padding-left:5px;line-height:11px">EMAIL ADDRESS</div>
  <div class="abs" style="left:388px;top:1130px;width:12px;height:12px;background:var(--blue);color:#fff;font-size:3.8px;display:flex;align-items:center;justify-content:center">GO</div>

  <div class="abs bottom">© 2017 Harbor Care Group . all right reserved.</div>
</div>
</body>
</html>
```